Online-Marketing-Material für Steuerberater und Unternehmensberater
Zielgruppe
Ich bin Steuerberater und Unternehmensberater, Business-Coach.
Meine Zielgruppe sind KMU, deren Mitarbeitern und die Geschäftsführung
Aufgabenstellung
Ich benötige ein Banner für Zunftlo, Filmaro und Plauderhof
folgende Stichworte sollen vorkommen:
- Steuerberatung
- Unternehmensberatung
- Organisationsentwicklung
- agile Arbeitsmethoden
- Employer Branding
- Business-Coaching
- Change Management

```html
<!DOCTYPE html>
<html lang="de">
<head>
<meta charset="utf-8">
<title>Banner-Set Steuer- und Unternehmensberatung</title>
<link rel="stylesheet" href="https://fonts.googleapis.com/css2?family=Poppins:wght@300;400;500;600&display=swap">
<style>
  :root {
    --sheet-bg: #efefef;
    --brand-blue: #2f5b99;
    --brand-blue-deep: #27497f;
    --brand-blue-light: #3a68a8;
    --accent-green: #7cc243;
    --tick-blue: #2a5cab;
    --text-dark: #1f2430;
    --city-light: #f5f6f8;
    --city-mid: #e2e6eb;
    --white: #ffffff;
  }
  * { box-sizing: border-box; margin: 0; padding: 0; }
  html, body { width: 1200px; height: 960px; overflow: hidden; }
  body {
    background: var(--sheet-bg);
    font-family: "Poppins", sans-serif;
    color: var(--text-dark);
    position: relative;
  }

  /* ---------- banner base ---------- */
  .banner {
    position: absolute;
    overflow: hidden;
    box-shadow: 0 2px 6px rgba(0,0,0,0.12);
  }
  .banner__city {
    position: absolute; inset: 0;
    background: linear-gradient(180deg, var(--city-light) 0%, var(--city-mid) 70%, #d9dee4 100%);
  }
  .banner__panel { position: absolute; inset: 0; width: 100%; height: 100%; }
  .banner__icon {
    position: absolute;
    background: linear-gradient(160deg, rgba(255,255,255,0.16), rgba(255,255,255,0.06));
    border-radius: 6px;
  }
  .headline {
    position: absolute;
    color: var(--white);
    font-weight: 300;
  }
  .headline__line { display: block; }
  .headline__accent { display: block; color: var(--accent-green); font-weight: 600; }
  .contact {
    position: absolute;
    color: var(--white);
    font-weight: 400;
  }
  .contact strong { font-weight: 600; }
  .services {
    position: absolute;
    list-style: none;
    display: grid;
    grid-auto-flow: column;
  }
  .services__item {
    display: flex;
    align-items: center;
    white-space: nowrap;
    color: var(--text-dark);
  }
  .services__tick { flex: none; color: var(--tick-blue); }
  .partner {
    position: absolute;
    display: flex;
    align-items: center;
    color: var(--brand-blue-deep);
    font-weight: 600;
    white-space: nowrap;
  }
  .partner__mark { background: var(--brand-blue-deep); flex: none; }

  /* ---------- Plauderhof ---------- */
  .banner--plauderhof { left: 63px; top: 83px; width: 418px; height: 184px; }
  .banner--plauderhof .banner__icon { left: 2px; top: 0; width: 116px; height: 130px; }
  .banner--plauderhof .headline { left: 128px; top: 22px; font-size: 18px; line-height: 22px; }
  .banner--plauderhof .contact { left: 129px; top: 137px; font-size: 7.5px; line-height: 10.5px; }
  .banner--plauderhof .services { left: 283px; top: 20px; grid-template-rows: repeat(7, 14.4px); font-size: 6.6px; }
  .banner--plauderhof .services__tick { width: 11px; height: 11px; margin-right: 3px; }
  .banner--plauderhof .partner { font-size: 6.5px; }
  .banner--plauderhof .partner__mark { width: 5px; height: 5px; margin-right: 3px; }

  /* ---------- Filmaro ---------- */
  .banner--filmaro { left: 63px; top: 314px; width: 1021px; height: 213px; }
  .banner--filmaro .banner__icon { left: 62px; top: 0; width: 176px; height: 180px; }
  .banner--filmaro .headline { left: 258px; top: 12px; font-size: 34px; line-height: 44px; }
  .banner--filmaro .headline__accent { font-size: 36px; }
  .banner--filmaro .contact { left: 262px; top: 158px; font-size: 14.5px; line-height: 19px; }
  .banner--filmaro .services { left: 556px; top: 23px; grid-template-rows: repeat(4, 25.8px); grid-template-columns: 190px 190px; font-size: 12.8px; }
  .banner--filmaro .services__tick { width: 22px; height: 22px; margin-right: 4px; }
  .banner--filmaro .partner { font-size: 11.5px; }
  .banner--filmaro .partner__mark { width: 8px; height: 8px; margin-right: 5px; }

  /* ---------- Zunftlo ---------- */
  .banner--zunftlo { left: 63px; top: 653px; width: 811px; height: 202px; }
  .banner--zunftlo .banner__icon { left: 0; top: 0; width: 178px; height: 185px; }
  .banner--zunftlo .headline { left: 200px; top: 10px; font-size: 32px; line-height: 40px; }
  .banner--zunftlo .headline__accent { font-size: 34px; }
  .banner--zunftlo .contact { left: 204px; top: 152px; font-size: 13.5px; line-height: 17.5px; }
  .banner--zunftlo .services { left: 463px; top: 30px; grid-template-rows: repeat(4, 24.5px); grid-template-columns: 182px 182px; font-size: 12px; }
  .banner--zunftlo .services__tick { width: 21px; height: 21px; margin-right: 3px; }
  .banner--zunftlo .partner { font-size: 11px; }
  .banner--zunftlo .partner__mark { width: 8px; height: 8px; margin-right: 5px; }

  /* ---------- format labels ---------- */
  .format-label { position: absolute; }
  .format-label__name { display: block; font-size: 20px; font-weight: 400; letter-spacing: 0.3px; line-height: 1.2; }
  .format-label__size { display: block; font-size: 33px; font-weight: 400; line-height: 1.2; margin-top: 6px; }
  .format-label--plauderhof { left: 534px; top: 96px; }
  .format-label--filmaro { left: 534px; top: 552px; }
  .format-label--zunftlo { left: 916px; top: 697px; }
</style>
</head>
<body>

<svg width="0" height="0" style="position:absolute" aria-hidden="true">
  <defs>
    <symbol id="tick" viewBox="0 0 24 24">
      <path d="M2 13 L8.5 19 L22 4 L9 15.5 Z" fill="currentColor"/>
    </symbol>
    <linearGradient id="panel-blue" x1="0" y1="0" x2="1" y2="1">
      <stop offset="0" stop-color="#2d5896"/>
      <stop offset="1" stop-color="#2a5192"/>
    </linearGradient>
  </defs>
</svg>

<!-- Plauderhof -->
<section class="banner banner--plauderhof">
  <div class="banner__city" role="img" aria-label="Helles Foto einer Stadtsilhouette"></div>
  <svg class="banner__panel" viewBox="0 0 418 184" preserveAspectRatio="none" role="img" aria-label="Blaue Fläche über einem Foto von Händen am Laptop">
    <path d="M0 0 H232 C258 50 262 130 232 184 H0 Z" fill="url(#panel-blue)"/>
  </svg>
  <div class="banner__icon" role="img" aria-label="Strichillustration: Dokument mit Dollarzeichen, Person und Sprechblase"></div>
  <h2 class="headline">
    <span class="headline__line">Verbessern</span>
    <span class="headline__line">Sie mit uns</span>
    <span class="headline__accent">Ihr Geschäft!</span>
  </h2>
  <p class="contact">Lindenhof 9 12345 Beispielstadt<br><strong>Tel:</strong> +49 1234 5678900</p>
  <ul class="services">
    <li class="services__item"><svg class="services__tick"><use href="#tick"/></svg>Steuerberatung</li>
    <li class="services__item"><svg class="services__tick"><use href="#tick"/></svg>Unternehmensberatung</li>
    <li class="services__item"><svg class="services__tick"><use href="#tick"/></svg>Organisationsentwicklung</li>
    <li class="services__item"><svg class="services__tick"><use href="#tick"/></svg>agile Arbeitsmethoden</li>
    <li class="services__item"><svg class="services__tick"><use href="#tick"/></svg>Employer Branding</li>
    <li class="services__item"><svg class="services__tick"><use href="#tick"/></svg>Business-Coaching</li>
    <li class="services__item"><svg class="services__tick"><use href="#tick"/></svg>Change Management</li>
  </ul>
  <div class="partner" style="left:274px;top:129px"><span class="partner__mark"></span>Brandt Steuer</div>
  <div class="partner" style="left:336px;top:129px"><span class="partner__mark"></span>Veltora</div>
  <div class="partner" style="left:294px;top:149px"><span class="partner__mark"></span>Hollmann &amp; Lenz</div>
</section>

<div class="format-label format-label--plauderhof">
  <span class="format-label__name">Plauderhof Cover</span>
  <span class="format-label__size">851 x 315</span>
</div>

<!-- Filmaro -->
<section class="banner banner--filmaro">
  <div class="banner__city" role="img" aria-label="Helles Foto einer Stadtsilhouette"></div>
  <svg class="banner__panel" viewBox="0 0 1021 213" preserveAspectRatio="none" role="img" aria-label="Blaue Fläche über einem Foto von Händen am Laptop">
    <path d="M0 0 H494 C525 60 527 150 497 213 H0 Z" fill="url(#panel-blue)"/>
  </svg>
  <div class="banner__icon" role="img" aria-label="Strichillustration: Dokument mit Dollarzeichen, Person und Sprechblase"></div>
  <h2 class="headline">
    <span class="headline__line">Verbessern</span>
    <span class="headline__line">Sie mit uns</span>
    <span class="headline__accent">Ihr Geschäft!</span>
  </h2>
  <p class="contact">Lindenhof 9 12345 Beispielstadt<br><strong>Tel:</strong> +49 1234 5678900</p>
  <ul class="services">
    <li class="services__item"><svg class="services__tick"><use href="#tick"/></svg>Steuerberatung</li>
    <li class="services__item"><svg class="services__tick"><use href="#tick"/></svg>Unternehmensberatung</li>
    <li class="services__item"><svg class="services__tick"><use href="#tick"/></svg>Organisationsentwicklung</li>
    <li class="services__item"><svg class="services__tick"><use href="#tick"/></svg>agile Arbeitsmethoden</li>
    <li class="services__item"><svg class="services__tick"><use href="#tick"/></svg>Employer Branding</li>
    <li class="services__item"><svg class="services__tick"><use href="#tick"/></svg>Business-Coaching</li>
    <li class="services__item"><svg class="services__tick"><use href="#tick"/></svg>Change Management</li>
  </ul>
  <div class="partner" style="left:548px;top:168px"><span class="partner__mark"></span>Brandt Steuer</div>
  <div class="partner" style="left:663px;top:168px"><span class="partner__mark"></span>Veltora</div>
  <div class="partner" style="left:760px;top:168px"><span class="partner__mark"></span>Hollmann &amp; Lenz</div>
</section>

<div class="format-label format-label--filmaro">
  <span class="format-label__name">Filmaro Cover</span>
  <span class="format-label__size">1855 x 423</span>
</div>

<!-- Zunftlo -->
<section class="banner banner--zunftlo">
  <div class="banner__city" role="img" aria-label="Helles Foto einer Stadtsilhouette"></div>
  <svg class="banner__panel" viewBox="0 0 811 202" preserveAspectRatio="none" role="img" aria-label="Blaue Fläche über einem Foto von Händen am Laptop">
    <path d="M0 0 H416 C446 55 448 140 420 202 H0 Z" fill="url(#panel-blue)"/>
  </svg>
  <div class="banner__icon" role="img" aria-label="Strichillustration: Dokument mit Dollarzeichen, Person und Sprechblase"></div>
  <h2 class="headline">
    <span class="headline__line">Verbessern</span>
    <span class="headline__line">Sie mit uns</span>
    <span class="headline__accent">Ihr Geschäft!</span>
  </h2>
  <p class="contact">Lindenhof 9 12345 Beispielstadt<br><strong>Tel:</strong> +49 1234 5678900</p>
  <ul class="services">
    <li class="services__item"><svg class="services__tick"><use href="#tick"/></svg>Steuerberatung</li>
    <li class="services__item"><svg class="services__tick"><use href="#tick"/></svg>Unternehmensberatung</li>
    <li class="services__item"><svg class="services__tick"><use href="#tick"/></svg>Organisationsentwicklung</li>
    <li class="services__item"><svg class="services__tick"><use href="#tick"/></svg>agile Arbeitsmethoden</li>
    <li class="services__item"><svg class="services__tick"><use href="#tick"/></svg>Employer Branding</li>
    <li class="services__item"><svg class="services__tick"><use href="#tick"/></svg>Business-Coaching</li>
    <li class="services__item"><svg class="services__tick"><use href="#tick"/></svg>Change Management</li>
  </ul>
  <div class="partner" style="left:462px;top:158px"><span class="partner__mark"></span>Brandt Steuer</div>
  <div class="partner" style="left:575px;top:158px"><span class="partner__mark"></span>Veltora</div>
  <div class="partner" style="left:668px;top:158px"><span class="partner__mark"></span>Hollmann &amp; Lenz</div>
</section>

<div class="format-label format-label--zunftlo">
  <span class="format-label__name">Zunftlo Cover</span>
  <span class="format-label__size">1584 x 396</span>
</div>

</body>
</html>
```